Business card for Eyelash extension salon in Beverly Hills,California USA

We need new business card for our salon in Beverly Hills. The salon name is 'Lumarra' . We would like to have...Business name: Lumarra Name of person: will provide later Address 6128 N.Corbel Ridge Blvd Verano Crest , CA 90999 Phone: will provide later (Text only) Web: www.lumarrastudio-example.com Pictogrid icon, Friendvale icon follow us for seasonal campaign and news @lumarrastudioexample Design should look elegant, high-end, clean, simple, cohesive with my brand. Please refer my brand board. Business name color will be metallic bronzy color. Im thinking grey background or white background. Thanks

Target Market(s)

25-35. Gender neutral. People who are in Entertainment business industry.
This is High-end Eyelash extension salon in Beverly Hills

Industry/Entity Type

Beauty Salon

Contact Information for Business Card

Business name: Lumarra
Name of person: will provide later
Address 6128 N.Corbel Ridge Blvd Verano Crest , CA 90999
Phone: will provide later (Text only)
Web: www.lumarrastudio-example.com
Pictogrid icon, Friendvale icon
follow us for seasonal campaign and news @lumarrastudioexample

Requirements
Must have
• Beautiful, elegant, clean and simple look but very attractive and modern
Should not have
• We don't like too clutter, too busy designs.

```html
<!DOCTYPE html>
<html lang="en">
<head>
<meta charset="utf-8">
<title>Lumarra – Business Card</title>
<link href="https://fonts.googleapis.com/css2?family=Playfair+Display:wght@400;500&display=swap" rel="stylesheet">
<style>
  :root {
    --backdrop: #f3b8b1;
    --card: #f7f7f7;
    --card-pattern: #ececec;
    --bronze: #7c6a56;
    --ink: #1d1d1d;
    --mark: #8a8a8a;
  }
  * { box-sizing: border-box; margin: 0; padding: 0; }
  html, body {
    width: 1200px; height: 801px; overflow: hidden;
    background: var(--backdrop);
    font-family: "Playfair Display", Georgia, serif;
  }
  .stage {
    position: relative; width: 1200px; height: 801px;
    display: flex; align-items: center; justify-content: center; gap: 50px;
  }
  .card {
    position: relative; width: 525px; height: 300px;
    background: var(--card);
    box-shadow: 0 6px 18px rgba(120, 60, 55, 0.18);
    overflow: hidden;
  }
  .card__pattern {
    position: absolute; inset: 0;
    background: linear-gradient(135deg, var(--card) 0%, var(--card-pattern) 50%, var(--card) 100%);
  }
  .brand-name {
    position: relative; color: var(--bronze);
    font-weight: 400; letter-spacing: 0.02em;
  }
  .card--front { display: flex; align-items: center; justify-content: center; }
  .card--front .brand-name { font-size: 64px; }

  .card--back { display: flex; padding: 34px 30px 30px 38px; gap: 24px; }
  .card--back .brand-name { font-size: 50px; align-self: flex-end; margin-bottom: 22px; }
  .contact {
    position: relative; flex: 1;
    display: flex; flex-direction: column; align-items: center; text-align: center;
    color: var(--ink); font-size: 13px; line-height: 1.45;
  }
  .contact__person { font-size: 21px; font-weight: 500; margin-bottom: 14px; }
  .contact__block { margin-bottom: 9px; }
  .contact__follow { font-size: 11px; margin-top: 6px; margin-bottom: 8px; }
  .socials { display: flex; gap: 18px; margin-bottom: 6px; }
  .social { display: flex; align-items: center; gap: 5px; font-size: 12px; }
  .social__square { width: 10px; height: 10px; background: var(--mark); }
</style>
</head>
<body>
<main class="stage">
  <section class="card card--front" aria-label="Card front">
    <div class="card__pattern" role="img" aria-label="Subtle pale grey concentric circle pattern"></div>
    <h1 class="brand-name">Lumarra</h1>
  </section>

  <section class="card card--back" aria-label="Card back">
    <div class="card__pattern" role="img" aria-label="Subtle pale grey concentric circle pattern"></div>
    <h2 class="brand-name">Lumarra</h2>
    <div class="contact">
      <p class="contact__person">Name</p>
      <p class="contact__block">6128<br>N.Corbel Ridge Blvd Verano Crest ,<br>CA 90999</p>
      <p class="contact__block">0000000000</p>
      <p>www.lumarrastudio-example.com</p>
      <p class="contact__follow">follow us for seasonal campaign and news</p>
      <div class="socials">
        <span class="social"><span class="social__square"></span>Pictogrid</span>
        <span class="social"><span class="social__square"></span>Friendvale</span>
      </div>
      <p>@lumarrastudioexample</p>
    </div>
  </section>
</main>
</body>
</html>
```